Webpage for balustrade importer and installer

We are a balustrade importer and installer. We sell a few different products mostly connected with glass and aluminum. We sell balconies, stairs, shower glass, mirrors, splash back glass, office partitions, glass dors and walls.

```html
<!DOCTYPE html>
<html lang="en">
<head>
<meta charset="utf-8">
<title>KLARVIK — Balustrade Importer and Installer</title>
<link href="https://fonts.googleapis.com/css2?family=Poppins:wght@300;400;500;600;800&display=swap" rel="stylesheet">
<style>
:root{
  --navy:#0b1a5c;
  --navy-deep:#0a1450;
  --footer:#16215e;
  --footer-card:#222d6b;
  --blue:#143c9e;
  --blue-mid:#1f47b0;
  --ring:#d6dcf0;
  --ring-inner:#c3cdea;
  --bg-soft:#f0f1f4;
  --text:#2b2f3c;
  --muted:#9aa3c8;
  --white:#ffffff;
  --highlight:#dfe6f7;
}
*{box-sizing:border-box;margin:0;padding:0}
html,body{width:1200px;height:3586px;overflow:hidden}
body{position:relative;font-family:"Poppins",sans-serif;color:var(--text);background:var(--white)}
.abs{position:absolute}
.btn{position:absolute;background:var(--navy);color:var(--white);font-size:13px;font-weight:500;display:flex;align-items:center;justify-content:center;gap:12px;box-shadow:5px 5px 0 #c9d0e6}
.btn svg{width:18px;height:18px}

/* hero */
.hero{position:absolute;left:0;top:0;width:1200px;height:612px;background:linear-gradient(180deg,#7fb6e4 0%,#b9d8ef 30%,#dbe8f1 45%,#a98a6c 58%,#8b6a4e 70%,#3aa6c8 80%,#1d8fb8 100%)}
.logo{position:absolute;font-family:"Poppins",sans-serif;font-weight:300;letter-spacing:1px;color:var(--navy)}
.hero .logo{left:81px;top:40px;font-size:38px}
.nav{position:absolute;top:58px;font-size:13px;color:var(--navy);font-weight:400}
.nav-contact{position:absolute;left:987px;top:42px;width:123px;height:50px;background:var(--navy);color:var(--white);font-size:13px;font-weight:500;display:flex;align-items:center;justify-content:center;box-shadow:4px 4px 0 #8fa5c9}
.hero-title{position:absolute;left:86px;top:372px;font-size:54px;font-weight:800;color:var(--navy);letter-spacing:1px}
.hero-sub{position:absolute;left:86px;top:452px;font-size:19px;color:#3b3f52;font-weight:400}
.slider-bars{position:absolute;left:1094px;top:292px;display:flex;gap:8px}
.slider-bars span{width:2px;height:28px;background:var(--navy)}
.slider-bars span+span{background:#9fb4c8}

/* section headings */
.sec-title{position:absolute;font-size:27px;font-weight:800;color:var(--blue);line-height:1}
.sec-title::after{content:"";position:absolute;left:0;right:-6px;bottom:-4px;height:10px;background:var(--highlight);z-index:-1}
.sec-sub{position:absolute;font-size:21px;color:var(--blue);font-weight:400}

/* services */
.services{position:absolute;left:0;top:612px;width:1200px;height:617px;background:var(--bg-soft);z-index:0}
.tile{position:absolute;color:var(--white);font-size:13px;font-weight:500}
.tile span{position:absolute;left:28px;bottom:30px}
.tile-bal{background:linear-gradient(180deg,#8d98ad 0%,#5f6f8e 55%,#1c2d74 100%)}
.tile-stairs{background:linear-gradient(180deg,#b5bac4 0%,#7d87a0 55%,#1c2d74 100%)}
.tile-shower{background:linear-gradient(180deg,#c8cdd8 0%,#8a94ae 55%,#1c2d74 100%)}
.tile-doors{background:linear-gradient(180deg,#c3c8d3 0%,#8992ac 55%,#1c2d74 100%)}
.tile-splash{background:linear-gradient(180deg,#a7a9ad 0%,#7a8c3a 45%,#3f4f6c 75%,#1c2d74 100%)}
.tile-office{background:linear-gradient(180deg,#c0c6d1 0%,#8891ab 55%,#1c2d74 100%)}

/* about */
.about-text{position:absolute;left:86px;width:675px;font-size:13.5px;line-height:21px;color:var(--text)}
.about-img{position:absolute;left:789px;top:1304px;width:325px;height:325px;background:linear-gradient(180deg,#1d3c9a 0%,#3d5ca8 45%,#6a7c9c 62%,#b0b6c1 80%,#c9cbd1 100%)}

/* features */
.ring{position:absolute;width:114px;height:114px;border-radius:50%;background:var(--ring);display:flex;align-items:center;justify-content:center}
.ring .core{width:66px;height:66px;border-radius:50%;background:var(--blue-mid);box-shadow:0 0 0 6px var(--ring-inner);display:flex;align-items:center;justify-content:center}
.ring svg{width:32px;height:32px}
.card{position:absolute;width:325px;height:181px;background:var(--white);box-shadow:0 4px 18px rgba(20,40,100,.08);text-align:center;padding:0 34px;display:flex;flex-direction:column;justify-content:center}
.card h3{font-size:16px;font-weight:500;color:var(--blue);margin-bottom:14px}
.card p{font-size:13.5px;line-height:22px;color:var(--text)}

/* projects */
.proj{position:absolute;top:2236px;width:231px;height:175px}
.p1{background:linear-gradient(180deg,#8c8d90,#c7b9a3 50%,#7a6b5a)}
.p2{background:linear-gradient(160deg,#5c5e62,#8d8f92 50%,#d9dadb)}
.p3{background:linear-gradient(170deg,#e6ecec,#bfd3cf 50%,#56707a)}
.p4{background:linear-gradient(180deg,#dcdcd8,#a8a597 50%,#54463a)}

/* worldwide */
.world{position:absolute;left:99px;top:2545px;width:1001px;height:394px;background:linear-gradient(180deg,#0b1853 0%,#0e1f64 60%,#16287a 100%);border-radius:6px;overflow:hidden;color:var(--white);text-align:center}
.world-map{position:absolute;left:60px;top:220px;width:880px;height:150px;border-radius:50%;background:radial-gradient(ellipse at center,rgba(60,90,190,.35),rgba(14,31,100,0) 70%)}
.tabs{position:absolute;left:278px;top:41px;display:flex;height:70px}
.tabs div{display:flex;align-items:center;justify-content:center;font-size:29px;font-weight:400;background:#1a3597;padding:0 28px}
.tabs div+div{background:#1e3ca8}
.world h2{position:absolute;left:0;right:0;top:150px;font-size:40px;font-weight:800;letter-spacing:.5px}
.world p{position:absolute;left:0;right:0;top:226px;font-size:20px}

/* stats */
.stats{position:absolute;left:0;top:2939px;width:1200px;height:221px;background:linear-gradient(180deg,#ffffff 0%,#e7e9f1 60%,#d5d8e5 100%)}
.stat-icon{position:absolute;top:3025px;width:58px;height:54px}
.stat-num{position:absolute;top:3024px;font-size:20px;color:var(--navy)}
.stat-lbl{position:absolute;top:3056px;font-size:13.5px;color:#3b3f52}

/* footer */
.footer{position:absolute;left:0;top:3160px;width:1200px;height:426px;background:var(--footer);color:var(--white)}
.fcard{position:absolute;top:3197px;width:329px;height:116px;background:var(--footer-card);padding:28px 28px}
.fcard h4{font-size:17px;font-weight:500;margin-bottom:14px}
.fcard p{font-size:13.5px}
.fcard svg{position:absolute;right:20px;top:30px;width:58px;height:58px;opacity:.35}
.footer-logo{left:99px;top:3358px;font-size:38px;color:var(--white)}
.f-about{position:absolute;left:99px;top:3429px;width:310px;font-size:13.5px;line-height:21px;color:var(--muted)}
.social{position:absolute;left:99px;top:3508px;width:220px;height:42px;background:var(--footer-card);display:flex;align-items:center;justify-content:space-around;padding:0 16px}
.social span{width:12px;height:12px;background:#b7bfe0;border-radius:2px}
.fcol h4{position:absolute;font-size:17px;font-weight:500;color:var(--white)}
.flink{position:absolute;font-size:13.5px;color:var(--muted)}
</style>
</head>
<body>

<!-- HERO -->
<header class="hero" role="img" aria-label="Glass balustrade on a wooden deck above a pool under a blue sky">
</header>
<div class="logo" style="left:81px;top:38px;font-size:38px">KLARVIK</div>
<nav>
  <span class="nav" style="left:594px">HOME</span>
  <span class="nav" style="left:676px">COMPANY</span>
  <span class="nav" style="left:788px">PRODUCTS</span>
  <span class="nav" style="left:903px">GALLERY</span>
  <span class="nav-contact">CONTACT</span>
</nav>
<div class="slider-bars"><span></span><span></span></div>
<h1 class="hero-title">BALUSTER</h1>
<p class="hero-sub">LEADER IN HOME IMPROVEMENT PRODUCTS</p>
<svg class="abs" style="left:86px;top:557px" width="26" height="24" viewBox="0 0 26 24" fill="none" stroke="#0b1a5c" stroke-width="2"><path d="M24 12H3M11 4L3 12l8 8"/></svg>
<svg class="abs" style="left:138px;top:557px" width="26" height="24" viewBox="0 0 26 24" fill="none" stroke="#0b1a5c" stroke-width="2"><path d="M2 12h21M15 4l8 8-8 8"/></svg>
<div class="btn" style="left:881px;top:530px;width:233px;height:50px;box-shadow:none">REVIEW OUR SERVICES
  <svg viewBox="0 0 20 20" fill="none" stroke="#fff" stroke-width="2"><path d="M4 7l6 6 6-6"/></svg></div>

<!-- SERVICES -->
<section class="services"></section>
<h2 class="sec-title" style="left:99px;top:672px">OUR SERVICES</h2>
<p class="sec-sub" style="left:99px;top:703px">Featured Solutions</p>
<div class="tile tile-bal" style="left:99px;top:763px;width:487px;height:191px" role="img" aria-label="Glass balcony on a modern building"><span>BALCONIES</span></div>
<div class="tile tile-stairs" style="left:612px;top:763px;width:232px;height:191px" role="img" aria-label="Staircase with glass railing"><span>STAIRS</span></div>
<div class="tile tile-shower" style="left:870px;top:763px;width:230px;height:191px" role="img" aria-label="Glass shower enclosure"><span>SHOWER GLASS</span></div>
<div class="tile tile-doors" style="left:99px;top:983px;width:231px;height:190px" role="img" aria-label="Frameless glass doors"><span>GLASS DOORS</span></div>
<div class="tile tile-splash" style="left:356px;top:983px;width:230px;height:190px" role="img" aria-label="Kitchen with green splash back glass"><span>SPLASH BACK GLASS</span></div>
<div class="tile tile-office" style="left:612px;top:983px;width:488px;height:190px" role="img" aria-label="Frosted glass office partitions"><span>OFFICE PARTITIONS</span></div>

<!-- ABOUT -->
<h2 class="sec-title" style="left:86px;top:1304px">ABOUT US</h2>
<p class="sec-sub" style="left:86px;top:1335px">Balustrade Importer and Installer</p>
<p class="about-text" style="top:1379px">Lorem ipsum dolor sit amet, consectetur adipiscing elit, sed do eiusmod tempor incididunt ut labore et dolore magna aliqua. Ut enim ad minim veniam, quis nostrud exercitation ullamco laboris nisi ut aliquip ex ea commodo consequat. Duis aute irure dolor in reprehenderit in voluptate velit esse cillum dolore eu fugiat nulla pariatur. Excepteur sint occaecat cupidatat non proident, sunt in culpa qui officia deserunt mollit anim id est laborum.</p>
<p class="about-text" style="top:1499px">Lorem ipsum dolor sit amet, consectetur adipiscing elit, sed do eiusmod tempor incididunt ut labore et dolore magna aliqua.</p>
<div class="btn" style="left:86px;top:1570px;width:170px;height:49px">MORE DETAIL
  <svg viewBox="0 0 20 20" fill="none" stroke="#fff" stroke-width="2"><path d="M3 10h13M11 5l5 5-5 5"/></svg></div>
<div class="about-img" role="img" aria-label="Glass balustrade on a terrace overlooking a city at dusk"></div>

<!-- FEATURES -->
<div class="ring" style="left:191px;top:1719px"><div class="core">
  <svg viewBox="0 0 32 32" fill="none" stroke="#fff" stroke-width="2.2"><path d="M16 4l10 4v7c0 7-5 11-10 13-5-2-10-6-10-13V8z"/><path d="M11 16l4 4 6-7"/></svg></div></div>
<div class="ring" style="left:543px;top:1719px"><div class="core">
  <svg viewBox="0 0 32 32" fill="none" stroke="#fff" stroke-width="2.2"><rect x="4" y="9" width="15" height="12" rx="1"/><path d="M19 13h5l4 4v4h-9"/><circle cx="10" cy="23" r="2.5"/><circle cx="23" cy="23" r="2.5"/></svg></div></div>
<div class="ring" style="left:894px;top:1719px"><div class="core">
  <svg viewBox="0 0 32 32" fill="none" stroke="#fff" stroke-width="2.2"><circle cx="16" cy="16" r="11"/><circle cx="12" cy="13" r=".8" fill="#fff"/><circle cx="20" cy="13" r=".8" fill="#fff"/><path d="M11 18c2 3 8 3 10 0"/></svg></div></div>

<div class="card" style="left:86px;top:1865px"><h3>HIGH DURABILITY</h3><p>We use the most exclusive and high quality products in railing manufacturing</p></div>
<div class="card" style="left:437px;top:1865px"><h3>FAST DELIVERY</h3><p>Your orders are processed quickly and delivered on the date you requested</p></div>
<div class="card" style="left:788px;top:1865px"><h3>CUSTOMER HAPPINESS</h3><p>Customer satisfaction is our top priority in all our services</p></div>

<!-- PROJECTS -->
<h2 class="sec-title" style="left:99px;top:2134px">RECENT PROJECTS</h2>
<p class="sec-sub" style="left:99px;top:2165px">Featured Solutions</p>
<div class="proj p1" style="left:99px" role="img" aria-label="Balcony with white glass railing"></div>
<div class="proj p2" style="left:356px" role="img" aria-label="Glass shower in a grey bathroom"></div>
<div class="proj p3" style="left:612px" role="img" aria-label="Frosted glass office partitions in a corridor"></div>
<div class="proj p4" style="left:870px" role="img" aria-label="Glass wall in a bright office interior"></div>
<div class="btn" style="left:906px;top:2439px;width:194px;height:50px">MORE PROJECTS
  <svg viewBox="0 0 20 20" fill="none" stroke="#fff" stroke-width="2"><path d="M3 10h13M11 5l5 5-5 5"/></svg></div>

<!-- WORLDWIDE -->
<section class="world">
  <div class="world-map" role="img" aria-label="Dotted world map background"></div>
  <div class="tabs"><div>5 Continent</div><div>+40 Country</div></div>
  <h2>KLARVIK WORLDWIDE</h2>
  <p>COUNTRIES WE EXPORT</p>
</section>

<!-- STATS -->
<section class="stats"></section>
<svg class="stat-icon" style="left:152px" viewBox="0 0 58 54"><path d="M2 2h54v36H24l-12 12V38H2z" fill="#0b1a5c"/><path d="M17 20l8 8 16-15" fill="none" stroke="#fff" stroke-width="4"/></svg>
<div class="stat-num" style="left:227px">15.000+</div><div class="stat-lbl" style="left:227px">Completed Service</div>
<svg class="stat-icon" style="left:493px" viewBox="0 0 58 54" fill="#0b1a5c"><path d="M29 2l26 12-26 12L3 14z"/><path d="M3 25l26 12 26-12v7L29 44 3 32z"/><path d="M3 37l26 12 26-12v5L29 54 3 42z"/></svg>
<div class="stat-num" style="left:568px">25+</div><div class="stat-lbl" style="left:568px">Years of Experience</div>
<svg class="stat-icon" style="left:868px" viewBox="0 0 58 54" fill="#0b1a5c"><circle cx="29" cy="14" r="10"/><circle cx="11" cy="19" r="7"/><circle cx="47" cy="19" r="7"/><path d="M13 50c0-12 7-20 16-20s16 8 16 20z"/><path d="M0 46c0-9 4-15 11-15 3 0 5 1 6 2-3 4-5 8-5 13z"/><path d="M58 46c0-9-4-15-11-15-3 0-5 1-6 2 3 4 5 8 5 13z"/></svg>
<div class="stat-num" style="left:955px">15+</div><div class="stat-lbl" style="left:955px">Our Staff</div>

<!-- FOOTER -->
<footer class="footer"></footer>
<div class="fcard" style="left:93px"><h4>Support</h4><p>(+00) 555 010 2040</p>
  <svg viewBox="0 0 58 58" fill="none" stroke="#9aa3c8" stroke-width="5"><path d="M10 36V28a19 19 0 0138 0v8"/><rect x="8" y="30" width="10" height="16" rx="4" fill="#9aa3c8"/><rect x="40" y="30" width="10" height="16" rx="4" fill="#9aa3c8"/></svg></div>
<div class="fcard" style="left:436px"><h4>E-Mail</h4><p>mail@klarvik.example</p>
  <svg viewBox="0 0 58 58" fill="#9aa3c8"><path d="M4 24L29 8l25 16v26H4z"/><path d="M4 24l25 16 25-16" fill="none" stroke="#222d6b" stroke-width="3"/></svg></div>
<div class="fcard" style="left:778px"><h4>Address</h4><p>120 Harbor Lane Eastfield</p>
  <svg viewBox="0 0 58 58" fill="#9aa3c8"><path d="M29 4a17 17 0 0117 17c0 13-17 33-17 33S12 34 12 21A17 17 0 0129 4z"/><circle cx="29" cy="21" r="6" fill="#222d6b"/></svg></div>

<div class="logo footer-logo">KLARVIK</div>
<p class="f-about">Lorem ipsum dolor sit amet, consectetur adipiscing elit, sed do eiusmod tempor incididunt ut labore et dolore magna aliqua.</p>
<div class="social" aria-label="Social links"><span></span><span></span><span></span><span></span></div>

<div class="fcol">
  <h4 style="left:468px;top:3358px">Company</h4>
  <span class="flink" style="left:468px;top:3403px">About</span>
  <span class="flink" style="left:468px;top:3431px">Our Vision</span>
  <span class="flink" style="left:468px;top:3459px">Our Mission</span>
  <span class="flink" style="left:468px;top:3487px">Gallery</span>
  <h4 style="left:810px;top:3358px">Services</h4>
  <span class="flink" style="left:810px;top:3403px">Stairs</span>
  <span class="flink" style="left:810px;top:3431px">Glass Doors</span>
  <span class="flink" style="left:810px;top:3459px">Shower Glass</span>
  <span class="flink" style="left:810px;top:3487px">Office Partitions</span>
</div>

</body>
</html>
```